Book Cover Design: Manuscript Mason's™ Roadmap: Indie-Release Essentials

I need a book cover designed for the first book in the "Manuscript Mason's™ Roadmap" series. Second book to follow in a few weeks and then we'll be rolling out 1-2 new titles per month throughout 2017.

The cover design should be something that can be replicated with a new subtitle, for the next books in the series.

The graphic designer’s work that is selected for my cover series will be given credit on the copyright page of the book(s).

Target Market(s)

Authors interested in self-publishing. Publishing.

Industry/Entity Type

Publishing

Font styles to use
Serif

Requirements
Must have
• Please see attached design instructions.
Nice to have
Should not have
• Cheesy book cover images on the cover.

```html
<!DOCTYPE html>
<html lang="en">
<head>
<meta charset="utf-8">
<title>Manuscript Mason's™ Roadmap: Indie-Release Essentials</title>
<link href="https://fonts.googleapis.com/css2?family=Bodoni+Moda:opsz,wght@6..96,600&family=Roboto:wght@400;500&display=swap" rel="stylesheet">
<style>
  :root {
    --paper: #ffffff;
    --ink: #1c1f22;
    --teal-deep: #4b6f79;
    --band: #5d7f87;
    --drafting-light: #e6eff5;
    --drafting-mid: #b9cfdf;
    --drafting-deep: #8eaec6;
  }
  * { margin: 0; padding: 0; box-sizing: border-box; }
  html, body {
    width: 928px; height: 1200px; overflow: hidden;
    background: var(--paper);
  }
  .cover {
    position: relative;
    width: 928px; height: 1200px;
    background: var(--paper);
  }
  .author {
    position: absolute; top: 70px; left: 0; right: 0;
    text-align: center;
    font-family: "Roboto", Arial, sans-serif;
    font-weight: 400;
    font-size: 50px;
    letter-spacing: 6px;
    color: var(--ink);
    text-transform: uppercase;
  }
  .title {
    position: absolute; top: 250px; left: 40px; right: 40px;
    text-align: center;
    font-family: "Bodoni Moda", "Times New Roman", serif;
    font-weight: 600;
    color: var(--teal-deep);
  }
  .title-line { display: block; line-height: 1.15; white-space: nowrap; }
  .title-series { font-size: 70px; }
  .title-main { font-size: 116px; margin-top: 10px; }
  .drafting-scene {
    position: absolute; top: 600px; left: 0; width: 928px; height: 395px;
    background: linear-gradient(180deg, var(--paper) 0%, var(--drafting-light) 22%, var(--drafting-mid) 60%, var(--drafting-deep) 100%);
  }
  .band-heavy {
    position: absolute; top: 995px; left: 0; width: 928px; height: 20px;
    background: var(--band);
  }
  .band-light {
    position: absolute; top: 1015px; left: 0; width: 928px; height: 30px;
    background: var(--drafting-mid);
  }
  .band-thin {
    position: absolute; top: 1045px; left: 0; width: 928px; height: 14px;
    background: var(--band);
  }
  .subtitle {
    position: absolute; top: 1092px; left: 0; right: 0;
    text-align: center;
    font-family: "Roboto", Arial, sans-serif;
    font-weight: 500;
    font-size: 38px;
    letter-spacing: 5px;
    color: var(--ink);
    text-transform: uppercase;
  }
</style>
</head>
<body>
  <main class="cover">
    <p class="author">Marla J. Penworth</p>
    <h1 class="title">
      <span class="title-line title-series">Manuscript Mason’s™</span>
      <span class="title-line title-main">Roadmap</span>
    </h1>
    <div class="drafting-scene" role="img" aria-label="Architectural blueprint drawings with a drafting compass, in soft blue tones"></div>
    <div class="band-heavy"></div>
    <div class="band-light"></div>
    <div class="band-thin"></div>
    <p class="subtitle">Indie-Release Essentials</p>
  </main>
</body>
</html>
```